Dane Calloway Photography

Would like the Business card to have a cool logo. I’m targeting wedding/ engagement: portrait photography. My phone number on it. And my business email address.

Target Market(s)

Wedding/portrait/engagement photography.

```html
<!DOCTYPE html>
<html lang="en">
<head>
<meta charset="utf-8">
<title>Dane Calloway Photography – Business Card</title>
<link rel="stylesheet" href="https://fonts.googleapis.com/css2?family=Montserrat:wght@300;400;600&family=Open+Sans:wght@400&display=swap">
<style>
  :root {
    --backdrop: #3b3b38;
    --card: #0e0e0f;
    --ink-white: #f2f2f2;
    --ink-soft: #b9b9b9;
    --ink-tonal: #2c2c2e;
    --ink-tonal-light: #3a3a3d;
  }
  * { margin: 0; padding: 0; box-sizing: border-box; }
  html, body {
    width: 1200px; height: 824px; overflow: hidden;
    background: var(--backdrop);
  }
  .sheet { position: relative; width: 1200px; height: 824px; }

  .card {
    position: absolute;
    width: 520px; height: 297px;
    background: var(--card);
    border-radius: 3px;
    box-shadow: 0 14px 30px rgba(0,0,0,.45);
  }
  .card--front { left: 50px; top: 90px; }
  .card--back { left: 630px; top: 90px; }

  .lockup { position: absolute; text-align: center; font-family: "Montserrat", sans-serif; }
  .lockup__mark {
    display: block; margin: 0 auto 14px;
    width: 14px; height: 14px; border-radius: 50%;
  }
  .lockup__name { font-weight: 600; letter-spacing: .02em; white-space: nowrap; }
  .lockup__sub { font-weight: 300; letter-spacing: .42em; text-transform: uppercase; }

  /* front: tonal spot-gloss logo */
  .card--front .lockup { left: 0; right: 0; top: 82px; }
  .card--front .lockup__mark { background: var(--ink-tonal-light); }
  .card--front .lockup__name { color: var(--ink-tonal-light); font-size: 30px; }
  .card--front .lockup__sub { color: var(--ink-tonal); font-size: 11px; margin-top: 4px; }
  .tagline {
    position: absolute; left: 34px; bottom: 34px;
    font-family: "Montserrat", sans-serif; font-size: 9.5px; font-weight: 400;
    letter-spacing: .06em; color: var(--ink-soft); text-transform: uppercase;
  }

  /* back */
  .card--back .lockup { left: 30px; width: 250px; top: 100px; }
  .card--back .lockup__mark { background: var(--ink-white); width: 10px; height: 10px; margin-bottom: 10px; }
  .card--back .lockup__name { color: var(--ink-white); font-size: 23px; }
  .card--back .lockup__sub { color: var(--ink-soft); font-size: 8px; margin-top: 3px; }

  .contact {
    position: absolute; left: 300px; top: 118px; list-style: none;
    font-family: "Open Sans", sans-serif; font-size: 13px; color: var(--ink-white);
  }
  .contact__item { display: flex; align-items: center; gap: 9px; height: 22px; }
  .contact__icon { width: 11px; height: 11px; fill: var(--ink-white); flex: none; }

  /* standalone logo */
  .sheet > .lockup { left: 50px; width: 260px; top: 560px; }
  .sheet > .lockup .lockup__mark { background: var(--ink-white); width: 16px; height: 16px; margin-bottom: 16px; }
  .sheet > .lockup .lockup__name { color: var(--ink-white); font-size: 26px; }
  .sheet > .lockup .lockup__sub { color: var(--ink-soft); font-size: 10.5px; margin-top: 8px; }
</style>
</head>
<body>
<main class="sheet">
  <section class="card card--front" aria-label="Business card front">
    <div class="lockup">
      <span class="lockup__mark"></span>
      <div class="lockup__name">DANE CALLOWAY</div>
      <div class="lockup__sub">Photography</div>
    </div>
    <p class="tagline">Wedding / Portrait / Engagement Photography</p>
  </section>

  <section class="card card--back" aria-label="Business card back">
    <div class="lockup">
      <span class="lockup__mark"></span>
      <div class="lockup__name">DANE CALLOWAY</div>
      <div class="lockup__sub">Photography</div>
    </div>
    <ul class="contact">
      <li class="contact__item">
        <svg class="contact__icon" viewBox="0 0 24 24"><path d="M6.6 10.8a15 15 0 0 0 6.6 6.6l2.2-2.2a1 1 0 0 1 1-.25 11.4 11.4 0 0 0 3.6.57 1 1 0 0 1 1 1V20a1 1 0 0 1-1 1A17 17 0 0 1 3 4a1 1 0 0 1 1-1h3.5a1 1 0 0 1 1 1c0 1.25.2 2.45.57 3.57a1 1 0 0 1-.25 1z"/></svg>
        <span>000 000 0000</span>
      </li>
      <li class="contact__item">
        <svg class="contact__icon" viewBox="0 0 24 24"><path d="M2 5h20v14H2z M2 5l10 8 10-8" fill="none" stroke="#f2f2f2" stroke-width="2.2"/></svg>
        <span>studio@danecalloway.photo</span>
      </li>
      <li class="contact__item">
        <svg class="contact__icon" viewBox="0 0 24 24"><g fill="none" stroke="#f2f2f2" stroke-width="2"><circle cx="12" cy="12" r="10"/><ellipse cx="12" cy="12" rx="4.5" ry="10"/><path d="M2 12h20M4 7h16M4 17h16"/></g></svg>
        <span>www.danecalloway.photo</span>
      </li>
    </ul>
  </section>

  <div class="lockup">
    <span class="lockup__mark"></span>
    <div class="lockup__name">DANE CALLOWAY</div>
    <div class="lockup__sub">Photography</div>
  </div>
</main>
</body>
</html>
```